A clean crisp business card for a Landscape Construction company. Designed to be easy to read contact/ info and also be appealing/interesting, unlike a traditional business card.

Industry/Entity Type

Landscape Construction

Contact Information for Business Card

Company name : Brambleway Landscape Construction, phone number: (877) 61Vista, website:Bramblewaylandscapes.example, Email, sales@bramblewaylandscapes.example

Requirements
Nice to have
• Luxurious finishes/ details…. Icons or emblems next to contact info
Should not have
• Clipart or general pictures

```html
<!DOCTYPE html>
<html lang="en">
<head>
<meta charset="utf-8">
<title>Brambleway Landscape Construction – Business Card</title>
<link rel="stylesheet" href="https://fonts.googleapis.com/css2?family=Montserrat:wght@500;600&family=Teko:wght@400&display=swap">
<style>
  :root {
    --page: #ffffff;
    --card-top: #151515;
    --card-bottom: #080808;
    --green: #9cca3c;
    --blue: #1a6bc1;
    --notch: #6e6e6e;
    --text: #ffffff;
    --radius: 40px;
  }
  * { margin: 0; padding: 0; box-sizing: border-box; }
  html, body {
    width: 1200px; height: 1200px; overflow: hidden;
    background: var(--page);
    font-family: "Montserrat", Arial, sans-serif;
  }
  .canvas { position: relative; width: 1200px; height: 1200px; }

  .card {
    position: absolute; left: 203px; width: 794px; height: 453px;
    border-radius: var(--radius); overflow: hidden;
    background: linear-gradient(180deg, var(--card-top), var(--card-bottom));
  }
  .card--front { top: 102px; }
  .card--back { top: 645px; }

  .bar { position: absolute; width: 68px; }
  .bar--green-top { left: 615px; top: 0; height: 201px; background: var(--green); border-radius: 0 0 34px 34px; }
  .bar--blue-bottom { left: 90px; top: 245px; bottom: 0; background: var(--blue); border-radius: 34px 34px 0 0; }
  .bar--notch { left: 355px; top: 0; height: 90px; background: var(--notch); border-radius: 0 0 34px 34px; }
  .bar--green-rail { left: 355px; top: 135px; bottom: 0; background: var(--green); border-radius: 34px 34px 0 0; }

  .brand { position: absolute; text-align: center; color: var(--green); font-weight: 600; line-height: 1.1; }
  .brand--front { left: 0; right: 0; top: 205px; }
  .brand--front .brand__name { font-size: 44px; letter-spacing: 1px; }
  .brand--front .brand__line { font-size: 17px; letter-spacing: 4px; text-transform: uppercase; margin-top: 4px; }
  .brand--back { right: 42px; top: 50px; }
  .brand--back .brand__name { font-size: 20px; }
  .brand--back .brand__line { font-size: 7.5px; letter-spacing: 1.5px; text-transform: uppercase; margin-top: 2px; }
  .brand__dot { display: block; width: 22px; height: 22px; border-radius: 50%; background: var(--green); margin: 0 auto 14px; }
  .brand--back .brand__dot { width: 12px; height: 12px; margin-bottom: 6px; }

  .person { position: absolute; right: 495px; top: 262px; text-align: right; color: var(--text); }
  .person__name { font-family: "Teko", "Arial Narrow", sans-serif; font-size: 68px; line-height: 0.9; letter-spacing: 5px; }
  .person__role { font-size: 21px; font-weight: 600; letter-spacing: 1px; margin-top: 4px; }

  .contact-icon { position: absolute; left: 380px; width: 20px; height: 20px; }
  .contact-text { position: absolute; left: 444px; color: var(--text); font-weight: 500; font-size: 18px; line-height: 25px; }
  .contact-text--small { font-size: 13px; font-weight: 600; }
</style>
</head>
<body>
<main class="canvas">

  <section class="card card--front" aria-label="Card front">
    <div class="bar bar--green-top"></div>
    <div class="bar bar--blue-bottom"></div>
    <div class="brand brand--front">
      <span class="brand__dot"></span>
      <div class="brand__name">Brambleway</div>
      <div class="brand__line">Landscape Construction</div>
    </div>
  </section>

  <section class="card card--back" aria-label="Card back">
    <div class="bar bar--notch"></div>
    <div class="bar bar--green-rail"></div>

    <div class="brand brand--back">
      <span class="brand__dot"></span>
      <div class="brand__name">Brambleway</div>
      <div class="brand__line">Landscape Construction</div>
    </div>

    <div class="person">
      <div class="person__name">YOUR NAME</div>
      <div class="person__role">Graphic Designer</div>
    </div>

    <svg class="contact-icon" style="top:223px" viewBox="0 0 20 20" aria-hidden="true">
      <path fill="var(--blue)" d="M10 1a6.5 6.5 0 0 0-6.5 6.5C3.5 12.5 10 19 10 19s6.5-6.5 6.5-11.5A6.5 6.5 0 0 0 10 1zm0 9a2.6 2.6 0 1 1 0-5.2A2.6 2.6 0 0 1 10 10z"/>
    </svg>
    <p class="contact-text" style="top:203px">4170 Larkmoor Valley Rd., NUM<br>310, Fernhollow, OH 45999</p>

    <svg class="contact-icon" style="top:274px" viewBox="0 0 20 20" aria-hidden="true">
      <path fill="var(--blue)" d="M4.5 2l3 3.5-1.8 2.2a11 11 0 0 0 6.6 6.6l2.2-1.8 3.5 3-1.6 2.5C9 18 2 11 2 3.6z"/>
    </svg>
    <p class="contact-text contact-text--small" style="top:272px">(562) 555 0187</p>

    <svg class="contact-icon" style="top:325px" viewBox="0 0 20 20" aria-hidden="true">
      <path fill="var(--blue)" d="M1 4h18v12H1z"/>
      <path fill="none" stroke="var(--card-bottom)" stroke-width="1.4" d="M1 4l9 7 9-7M1 16l6.5-6M19 16l-6.5-6"/>
    </svg>
    <p class="contact-text" style="top:322px">jo@bramblewaylandscapes.example</p>

    <svg class="contact-icon" style="top:375px" viewBox="0 0 20 20" aria-hidden="true">
      <path fill="var(--blue)" d="M4 1l12 10.5-5.2.6 3 6-2.4 1.2-3-6L4 17z"/>
    </svg>
    <p class="contact-text" style="top:373px">bramblewaylandscapes.example</p>
  </section>

</main>
</body>
</html>
```